One of a Kind Clean Business Card

We need to design a new business card template for our company. Our company designs and produced merchandising displays. You can see a sample of what we produce on our site www.qorvatfixtures.com. I have uploaded our logo in vector format, as well as a picture of our current business cards. We want a totally different look. We want simple and clean, looking forward to seeing what people create.
Updates

I would like to update the address for Tellur Display Group Inc. 418 N Brindle Ave Arlington Heights, IL 60817 Would also note. No QR codes

Industry/Entity Type

Business

Contact Information for Business Card

Need a 1 sided business card designed.

Font styles to use
Serif

Requirements
Must have
• Easy to view; Clean Design
Nice to have
• Features that promote engineering and creativity
Should not have
• Too much clutter, keep it simple

```html
<!DOCTYPE html>
<html lang="en">
<head>
<meta charset="utf-8">
<title>Tellur Display Group Inc. — Business Card</title>
<link rel="stylesheet" href="https://fonts.googleapis.com/css2?family=Montserrat:wght@400;500;700&display=swap">
<style>
  :root {
    --stage: #1e1e1e;
    --card: #ffffff;
    --ink: #111111;
    --muted: #7a7a7a;
    --accent: #8b1419;
    --rule: #222222;
  }
  * { box-sizing: border-box; margin: 0; padding: 0; }
  html, body { width: 1200px; height: 833px; overflow: hidden; }
  body {
    background: var(--stage);
    font-family: "Montserrat", Arial, sans-serif;
    display: flex;
    align-items: center;
    justify-content: center;
    gap: 60px;
  }
  .card {
    position: relative;
    width: 525px;
    height: 300px;
    background: var(--card);
    box-shadow: 0 12px 30px rgba(0,0,0,.55);
  }
  .brand {
    display: flex;
    align-items: center;
    gap: 8px;
    color: var(--accent);
    font-weight: 500;
    font-size: 19px;
    letter-spacing: .2px;
  }
  .brand-mark { width: 12px; height: 12px; background: var(--accent); flex: none; }

  /* Front */
  .card-front .brand { position: absolute; left: 34px; top: 128px; }
  .card-front .web {
    position: absolute; right: 28px; bottom: 22px;
    color: var(--muted); font-size: 12px;
  }

  /* Back */
  .card-back .person { position: absolute; left: 34px; top: 44px; }
  .person-name { color: var(--ink); font-weight: 700; font-size: 20px; }
  .person-title { color: var(--muted); font-size: 13px; margin-top: 2px; }
  .divider {
    position: absolute; left: 34px; right: 26px; top: 128px;
    border-top: 1px solid var(--rule);
  }
  .card-back .brand { position: absolute; right: 26px; top: 80px; font-size: 17px; }
  .contacts {
    position: absolute; left: 34px; top: 142px;
    list-style: none; color: var(--muted); font-size: 12.5px; line-height: 19px;
  }
  .contacts li { display: flex; align-items: center; gap: 7px; }
  .contacts svg { width: 11px; height: 11px; fill: var(--accent); flex: none; }
  .address {
    position: absolute; right: 26px; bottom: 26px;
    text-align: right; font-style: normal;
    color: var(--muted); font-size: 13px; line-height: 18px;
  }
  .address-company { color: var(--accent); font-weight: 700; }
</style>
</head>
<body>
  <section class="card card-front">
    <div class="brand"><span class="brand-mark"></span>Tellur Display Group Inc.</div>
    <div class="web">www.qorvatfixtures.com</div>
  </section>

  <section class="card card-back">
    <div class="person">
      <div class="person-name">Dale Morven</div>
      <div class="person-title">President</div>
    </div>
    <div class="brand"><span class="brand-mark"></span>Tellur Display Group Inc.</div>
    <div class="divider"></div>
    <ul class="contacts">
      <li><svg viewBox="0 0 16 16"><path d="M3 1l3 3-2 2c1 2 3 4 5 5l2-2 3 3-2 3C6 15 1 10 1 3z"/></svg>815-555-0142</li>
      <li><svg viewBox="0 0 16 16"><path d="M4 0h8v16H4zM6 2v10h4V2z"/></svg>312-555-0187</li>
      <li><svg viewBox="0 0 16 16"><path d="M0 3h16v10H0zM1 4l7 5 7-5z" fill-rule="evenodd"/></svg>dmorven@qorvatfixtures.com</li>
      <li><svg viewBox="0 0 16 16"><circle cx="8" cy="8" r="7.5"/></svg>www.qorvatfixtures.com</li>
    </ul>
    <address class="address">
      <div class="address-company">Tellur Display Group Inc.</div>
      <div>418 N Brindle Ave</div>
      <div>Arlington Heights</div>
      <div>IL 60817</div>
    </address>
  </section>
</body>
</html>
```